Cover for "ROOTED! The skill and rhythm of guiding teams through calm and delight"

My first book for a global audience of modern performance leaders needs its cover!
I am an international executive coach and I've developed a new approach to replace classic Performance Management with a natural, sustainable approach fit for human beings :) My first book is about this approach and serves two purposes: helping leaders and sparking their curiosity to learn more, and positioning myself as a thought leader in the field.
The book is built on personal experience; it is both professional and personal ("From me to You"), and I'd like to position it beyond classic categorisation.
Its cover should communicate humanness, naturalness, ease and joy, within an unmistakably business-y context. I would like to see designs that use the color yellow (but not sure it communicates the right things).
Updates

Target Market(s)

Leaders who aspire to have a positive impact and deliver results in a meaningful way

Industry/Entity Type

Consulting & Executive Coaching - Trusted Advisor

Font styles to use
Other font styles liked:
• Helvetica Neue

Colors
0094D4
00A9DD
6FCCEA
C7EBF8
E9F6FB
FFC000
F8CF3A
FAE287
FDF2CF
FEFAEE
EE7325
F08F49
F5BC92
FAE3D3
FDF4ED

Requirements
Must have
• A both-and feeling to it (see description), e.g., masculine AND feminine, business AND humanness. Power with, not power over...
Should not have
• Too much "bling" - no classic status symbol business success language

```html
<!DOCTYPE html>
<html lang="en">
<head>
<meta charset="utf-8">
<title>ROOTED! The skill and rhythm of guiding teams through calm and delight — Book Cover</title>
<link rel="stylesheet" href="https://fonts.googleapis.com/css2?family=Antonio:wght@700&family=League+Spartan:wght@800&display=swap">
<style>
  :root {
    --cover-ink: #1f1f1f;
    --cover-yellow: #ffc111;
  }
  html, body {
    margin: 0;
    padding: 0;
    width: 854px;
    height: 1200px;
    overflow: hidden;
    background: var(--cover-ink);
  }
  .book-cover {
    width: 854px;
    height: 1200px;
    display: block;
    background: var(--cover-ink);
  }
  .author-name,
  .subtitle-line,
  .subtitle-link {
    font-family: "Antonio", "Oswald", sans-serif;
    font-weight: 700;
    fill: var(--cover-yellow);
  }
  .author-name { font-size: 88px; }
  .subtitle-line { font-size: 60px; letter-spacing: 0.32em; }
  .subtitle-link { font-size: 32px; letter-spacing: 0.2em; }
  .book-title {
    font-family: "League Spartan", "Montserrat", sans-serif;
    font-weight: 800;
    font-size: 285px;
    fill: var(--cover-yellow);
  }
  .divider-rule { fill: var(--cover-yellow); }
</style>
</head>
<body>
<svg class="book-cover" viewBox="0 0 854 1200" xmlns="http://www.w3.org/2000/svg" aria-label="ROOTED! The skill and rhythm of guiding teams through calm and delight, by Marlo Vennick">
  <rect width="854" height="1200" fill="var(--cover-ink)"/>

  <text class="author-name" x="114" y="231" textLength="626" lengthAdjust="spacing">MARLO VENNICK</text>

  <text class="book-title" x="50" y="606" textLength="754" lengthAdjust="spacingAndGlyphs">ROOTED</text>

  <g class="subtitle">
    <text class="subtitle-line" x="434" y="816" text-anchor="middle" textLength="620" lengthAdjust="spacing">THE SKILL AND RHYTHM</text>

    <rect class="divider-rule" x="107" y="847" width="252" height="3"/>
    <text class="subtitle-link" x="430" y="865" text-anchor="middle">OF</text>
    <rect class="divider-rule" x="500" y="847" width="247" height="3"/>

    <text class="subtitle-line" x="434" y="924" text-anchor="middle" textLength="560" lengthAdjust="spacing">GUIDING TEAMS</text>

    <rect class="divider-rule" x="107" y="956" width="252" height="3"/>
    <text class="subtitle-link" x="430" y="968" text-anchor="middle">THROUGH</text>
    <rect class="divider-rule" x="500" y="956" width="247" height="3"/>

    <text class="subtitle-line" x="434" y="1035" text-anchor="middle" textLength="600" lengthAdjust="spacing">CALM AND DELIGHT.</text>
  </g>
</svg>
</body>
</html>
```